Letterhead

I would like a standard letter head document that is innovative and not 'typically' corporate.
I would like a BLACK panel of some sort so that the logo can be best showcased within that (as the logo has a black background).
I would like the three words 'dream', 'believe', 'achieve'
inscribed at the side (as per the example I uploaded). Its should be more like a watermark so only just visible.
I would like the K symbol as a water mark on the page (similar to the lion on the example I uploaded).
I would like the following details also included.
Lydia Thornbury
Personal Training/Nutrition/Life Coaching
www.strongandsteady.com.au
0417 256 094

```html
<!DOCTYPE html>
<html lang="en">
<head>
<meta charset="UTF-8">
<title>Strong and Steady – Letterhead</title>
<link href="https://fonts.googleapis.com/css2?family=Exo+2:wght@300;400;600&display=swap" rel="stylesheet">
<style>
  :root {
    --backdrop: #e6e6e4;
    --paper: #ffffff;
    --panel: #050505;
    --accent: #3cc7cf;
    --ink-light: #f2f2f2;
    --whisper: #3a3f40;
    --mark-tint: #e3efee;
  }
  * { box-sizing: border-box; margin: 0; padding: 0; }
  html, body {
    width: 1200px; height: 738px; overflow: hidden;
    background: var(--backdrop);
    font-family: "Exo 2", sans-serif;
  }
  .canvas {
    width: 1200px; height: 738px;
    display: flex; align-items: center; justify-content: center;
  }
  .letterhead {
    position: relative;
    width: 480px; height: 680px;
    background: var(--paper);
    box-shadow: 0 6px 24px rgba(0,0,0,0.18);
    overflow: hidden;
  }
  .watermark {
    position: absolute;
    left: 0; top: 190px;
    width: 300px;
    font-size: 60px; font-weight: 600; line-height: 1;
    color: var(--mark-tint);
    letter-spacing: 2px;
    text-align: center;
  }
  .brand-panel {
    position: absolute;
    top: 0; right: 0;
    width: 180px; height: 100%;
    background: var(--panel);
    display: flex; flex-direction: column; align-items: flex-end;
    padding: 34px 16px 30px;
  }
  .brand-name {
    display: flex; align-items: center; gap: 6px;
    font-size: 12px; font-weight: 600; color: var(--accent);
    letter-spacing: 0.5px; text-transform: uppercase;
    white-space: nowrap;
  }
  .brand-dot { width: 7px; height: 7px; border-radius: 50%; background: var(--accent); flex: none; }
  .brand-tagline {
    margin-top: 4px;
    font-size: 7px; letter-spacing: 1.6px; color: var(--accent);
    text-transform: uppercase; white-space: nowrap;
  }
  .values {
    margin-top: 150px;
    display: flex; flex-direction: column; align-items: flex-end; gap: 56px;
    font-size: 20px; font-weight: 300; color: var(--whisper);
  }
  .contact {
    margin-top: auto;
    text-align: right;
    font-style: normal;
    color: var(--ink-light);
    font-size: 9px; line-height: 1.5; letter-spacing: 0.3px;
    max-width: 148px;
  }
  .contact-name { color: var(--accent); font-size: 11px; font-weight: 600; margin-bottom: 8px; white-space: nowrap; }
  .contact-role { margin-bottom: 8px; }
  .contact-line { white-space: nowrap; }
</style>
</head>
<body>
  <main class="canvas">
    <article class="letterhead">
      <div class="watermark" aria-hidden="true">Strong and Steady</div>
      <aside class="brand-panel">
        <div class="brand-name"><span class="brand-dot"></span>Strong and Steady</div>
        <div class="brand-tagline">Personal Training</div>
        <div class="values">
          <span>Dream</span>
          <span>Believe</span>
          <span>Achieve</span>
        </div>
        <address class="contact">
          <p class="contact-name">Lydia Thornbury</p>
          <p class="contact-role">Personal<br>Training/Nutrition/Life<br>Coaching</p>
          <p class="contact-line">www.strongandsteady.com.au</p>
          <p class="contact-line">0417 256 094</p>
        </address>
      </aside>
    </article>
  </main>
</body>
</html>
```